Flyer for annual KESTREL SUMMIT 2020

I would like a church event flyer designed. The event is called "KESTREL SUMMIT 2020". I am looking for a professional, yet catchy design that uses our brand colors and logo creatively while communicating key information of the event effectively.

1. The logo is attached in two color formats. The designer has the choice to use them as he/she want.

2. The location of the event is: Harlow Community Center, 239 Fennimore Street, Portland, ME 04117

3. Time and date of event. The designer can organize and format the date and time as he/she pleases.
Thursday December 31st @ 6:30PM
Friday January 1st @ 6:30PM
Saturday 2nd @ 6:30PM
Sunday 3rd @ 4:30PM

4. The topic of the event is "In Fire and On Fire". The designer is free to use this phrase as he/she pleases to create a good composition.

5. Speaker: Prophet Marcus Olunde (2 pictures of the speaker to choose from are attached)

6. Contact information: contact@brightmeadowfold.org - Telephone number: 207 583 2914

7. I would also like the following three words on the flyer. These words describe the focus of the event: FIRE, REVIVAL, PROPHETIC

Target Market(s)

Young adults

Font styles to use
Sans Serif

Requirements
Must have
• Logo, speaker's picture
Should not have
• cross image, church image

```html
<!DOCTYPE html>
<html lang="en">
<head>
<meta charset="utf-8">
<title>Kestrel Summit 2020 Flyer</title>
<link href="https://fonts.googleapis.com/css2?family=Josefin+Sans:wght@600&family=Montserrat:ital,wght@0,400;0,700;1,700&family=Oswald:wght@300;600&display=swap" rel="stylesheet">
<style>
  :root {
    --navy: #12294a;
    --orange: #f7941d;
    --white: #ffffff;
    --peach: #fde9d6;
    --red: #e0302c;
    --stage: #ececec;
  }
  * { margin: 0; padding: 0; box-sizing: border-box; }
  html, body { width: 1200px; height: 1200px; overflow: hidden; background: var(--stage); }
  .flyer-frame { position: absolute; left: 160px; top: 30px; width: 880px; height: 1139px; overflow: hidden; }
  .flyer {
    position: absolute; left: 0; top: 0; width: 915px; height: 1184px;
    transform: scale(0.9617); transform-origin: top left;
    background: linear-gradient(180deg, var(--white) 55%, var(--peach) 85%, var(--white) 100%);
    font-family: "Montserrat", sans-serif; color: var(--navy);
    overflow: hidden;
  }
  .shapes { position: absolute; left: 0; top: 0; }
  .abs { position: absolute; }

  .brand { left: 612px; top: 118px; display: flex; align-items: center; gap: 12px; white-space: nowrap; }
  .brand-dot { width: 24px; height: 24px; border-radius: 50%; background: var(--orange); flex: none; }
  .brand-name { font-family: "Montserrat", sans-serif; font-weight: 400; font-size: 44px; color: var(--white); letter-spacing: 1px; line-height: 1; }

  .title { left: 55px; top: 250px; font-family: "Josefin Sans", sans-serif; font-weight: 600; line-height: 0.88; }
  .title-top { font-size: 96px; color: var(--orange); display: block; letter-spacing: -2px; }
  .title-mid { font-size: 96px; color: var(--white); display: block; letter-spacing: -2px; }
  .title-year { font-size: 88px; color: var(--orange); display: block; letter-spacing: -2px; margin-top: 6px; }
  .focus { left: 55px; top: 515px; font-weight: 700; font-style: italic; font-size: 30px; color: var(--white); letter-spacing: 0.5px; }

  .theme-card {
    left: 565px; top: 240px; width: 262px; height: 230px; background: var(--white);
    transform: rotate(-8deg); box-shadow: 4px 6px 10px rgba(0,0,0,0.25);
    font-family: "Oswald", sans-serif; text-align: center; color: var(--navy);
  }
  .theme-line { font-weight: 600; font-size: 66px; line-height: 1; display: block; margin-top: 22px; }
  .theme-line + .theme-line { margin-top: 0; }
  .theme-and { display: block; margin: 8px auto; width: 150px; background: var(--orange); color: var(--white); font-weight: 300; font-size: 32px; letter-spacing: 12px; line-height: 1.3; }
  .pin { left: 668px; top: 220px; width: 26px; height: 26px; border-radius: 50%; background: var(--red); box-shadow: 2px 3px 4px rgba(0,0,0,0.3); }

  .session { display: flex; align-items: center; gap: 12px; }
  .time-box { width: 113px; height: 66px; background: var(--white); position: relative; font-weight: 700; color: var(--orange); }
  .time-hour { position: absolute; left: 8px; top: 0; font-size: 60px; line-height: 66px; }
  .time-min { position: absolute; left: 45px; top: 4px; font-size: 34px; line-height: 1; }
  .time-ampm { position: absolute; left: 62px; top: 40px; font-size: 18px; line-height: 1; }
  .day { font-weight: 700; font-size: 18px; display: block; }
  .date { font-weight: 400; font-size: 18px; display: block; }

  .venue { left: 55px; top: 890px; font-weight: 700; font-size: 33px; white-space: nowrap; }
  .address { left: 55px; top: 935px; font-size: 21px; white-space: nowrap; }

  .contact-tab { left: 55px; top: 1006px; width: 341px; height: 58px; background: var(--orange); color: var(--white); font-size: 22px; line-height: 58px; padding-left: 18px; }
  .email { left: 55px; top: 1078px; font-size: 22px; }
  .phone { left: 55px; top: 1108px; font-size: 22px; }
  .phone strong { font-weight: 700; }

  .speaker-label { right: 52px; top: 1064px; font-weight: 700; font-size: 29px; color: var(--orange); text-align: right; }
  .speaker-name { right: 52px; top: 1100px; font-weight: 700; font-size: 31px; text-align: right; white-space: nowrap; }
</style>
</head>
<body>
<div class="flyer-frame">
  <div class="flyer">
    <svg class="shapes" width="915" height="1184" viewBox="0 0 915 1184">
      <defs>
        <radialGradient id="doveGlow" cx="0.35" cy="0.35" r="0.6">
          <stop offset="0" stop-color="#2f8aa0" stop-opacity="0.75"/>
          <stop offset="1" stop-color="#12294a" stop-opacity="0"/>
        </radialGradient>
        <linearGradient id="speakerTone" x1="0" y1="0" x2="0" y2="1">
          <stop offset="0" stop-color="#4a3328"/>
          <stop offset="0.35" stop-color="#2a1e1a"/>
          <stop offset="0.6" stop-color="#c9482a"/>
          <stop offset="1" stop-color="#b83e24"/>
        </linearGradient>
      </defs>
      <path d="M0,118 Q150,40 310,0 L915,0 L915,375 C720,450 520,700 220,652 C120,636 50,622 0,610 Z" fill="var(--navy)"/>
      <path d="M0,118 Q150,40 310,0 L915,0 L915,375 C720,450 520,700 220,652 C120,636 50,622 0,610 Z" fill="url(#doveGlow)" role="img" aria-label="Soft teal photo of a dove in flight among flames"/>
      <path d="M0,0 L310,0 Q150,40 0,118 Z" fill="var(--orange)"/>
      <path d="M650,700 C630,640 640,560 690,515 C740,475 810,500 820,570 C828,620 815,665 800,700 C850,720 900,740 915,760 L915,925 C820,975 720,1005 600,1022 C605,900 620,790 650,700 Z" fill="url(#speakerTone)" role="img" aria-label="Photo of the speaker, Prophet Marcus Olunde, in a red blazer"/>
      <path d="M395,1040 C600,1030 800,990 915,918 L915,958 C800,1012 600,1042 395,1046 Z" fill="var(--orange)"/>
    </svg>

    <div class="abs brand">
      <span class="brand-dot"></span>
      <span class="brand-name">VERANTH</span>
    </div>

    <h1 class="abs title">
      <span class="title-top">KESTREL</span>
      <span class="title-mid">SUMMIT</span>
      <span class="title-year">2020</span>
    </h1>
    <p class="abs focus">Fire,&nbsp; Revival, Prophetic</p>

    <div class="abs theme-card">
      <span class="theme-line">IN FIRE</span>
      <span class="theme-and">AND</span>
      <span class="theme-line">ON FIRE</span>
    </div>
    <div class="abs pin"></div>

    <div class="abs session" style="left:55px; top:700px;">
      <div class="time-box"><span class="time-hour">6</span><span class="time-min">:30</span><span class="time-ampm">PM</span></div>
      <div><span class="day">Thursday</span><span class="date">December 31st</span></div>
    </div>
    <div class="abs session" style="left:335px; top:700px;">
      <div class="time-box"><span class="time-hour">6</span><span class="time-min">:30</span><span class="time-ampm">PM</span></div>
      <div><span class="day">Saturday</span><span class="date">January 2nd</span></div>
    </div>
    <div class="abs session" style="left:55px; top:802px;">
      <div class="time-box"><span class="time-hour">6</span><span class="time-min">:30</span><span class="time-ampm">PM</span></div>
      <div><span class="day">Friday</span><span class="date">January 1st</span></div>
    </div>
    <div class="abs session" style="left:335px; top:802px;">
      <div class="time-box"><span class="time-hour">4</span><span class="time-min">:30</span><span class="time-ampm">PM</span></div>
      <div><span class="day">Sunday</span><span class="date">January 3rd</span></div>
    </div>

    <p class="abs venue">HARLOW Community Center</p>
    <p class="abs address">239 Fennimore Street, Portland, ME 04117</p>

    <div class="abs contact-tab">CONTACT INFORMATION:</div>
    <p class="abs email">contact@brightmeadowfold.org</p>
    <p class="abs phone"><strong>207 583 2914 |</strong> www.<strong>veranth</strong>.org</p>

    <p class="abs speaker-label">SPEAKER:</p>
    <p class="abs speaker-name">Prophet Marcus Olunde</p>
  </div>
</div>
</body>
</html>
```